Texas Marsh Reed Conservation League

We need to design the home page of this new website. We would like a fun website design for provides as a resource for members and information for potential members.
Please design so that we can see a portion of background on each side on the website.
I just need the final design files psd no coding needed.
Attached is their logo (colors are not 100% set in stone either so can mess with those as I did in the quick mockup attached)
Attached is a pdf newsletter they send out, you can get a feel for them and what they are about. The design is crappy and we are here to fix that going forward and we are starting with the website.
Here are some quick example websites (design style is open)
- I attached a quick mockup i did just for a content visual but by all means do what you want.
- http://www.lonestarbizladies.org/
- http://www.wqrtf.org/
- http://demo.webkitpalette.com/demo.php?cat=html5themes&host=layoutbazaar&temp=veltrona
- http://www.fieldkeep.org/
- http://www.urbanpantry.org/
- http://www.projectcozy.org/
here are some of the other chapters website (pretty bad!)
and here are some of the others:
- http://www.kdwrcl.org/
- http://wrcl.org/
- http://www.gwrcl.org/
Content Items that need to be included:
1. Logo
2. Menu - home, about, members, resources, events, membership, contact
3. Become a member - button or action
4. social links - facebook, linkedin, youtube
5. banner - that needs to explain their purpose "Promoting environmental stewardship through operations, research, education and outreach" (or this can be worked into the design)
6. Upcoming event (s)
7. Advertisement - members can place an ad on the website, this can be a placeholder for now
8. newsletter signup
9. advertise with us - this link can be in the footer
30-60 years of age, succesfull (household budgets of 120K+ men and women that live in texas.
Education

```html
<!DOCTYPE html>
<html lang="en">
<head>
<meta charset="utf-8">
<title>Texas Marsh Reed Conservation League</title>
<link href="https://fonts.googleapis.com/css2?family=Merriweather:wght@400;700&family=Arimo:wght@400;700&family=Open+Sans:wght@400;600&display=swap" rel="stylesheet">
<style>
:root{
  --navy:#0c1f4f;
  --navy-deep:#081a45;
  --maroon:#8c2438;
  --brown-head:#6b2a10;
  --rose:#a0566c;
  --copper:#a36a3a;
  --sky-top:#8dc3ee;
  --sky-mid:#bfe0f7;
  --grass:#8fc24a;
  --grass-deep:#5d9a2c;
  --panel:rgba(236,245,252,.82);
  --text:#1b1b1b;
  --rule:#7d8a99;
  --white:#fff;
}
*{margin:0;padding:0;box-sizing:border-box}
html,body{width:1182px;height:1200px;overflow:hidden}
body{position:relative;font-family:"Arimo",Arial,sans-serif;color:var(--text)}
.scenery{position:absolute;inset:0;background:linear-gradient(180deg,var(--sky-top) 0%,var(--sky-mid) 45%,#cfe8c8 62%,var(--grass) 78%,var(--grass-deep) 100%)}
.abs{position:absolute}
.logo{left:138px;top:46px;display:flex;align-items:center;gap:8px;font-family:"Merriweather",serif;font-weight:700;font-size:40px;color:var(--navy)}
.logo-dot{width:18px;height:18px;background:var(--maroon);border-radius:50%}
.site-title{left:349px;top:70px;font-family:"Merriweather",serif;font-weight:700;font-size:16px;color:var(--navy-deep);letter-spacing:.2px}
.social{display:flex;gap:5px}
.social span{width:25px;height:25px;border-radius:50%;background:var(--navy-deep);display:block}
.social-top{left:718px;top:5px}
.join{left:872px;top:0;width:171px;height:32px;background:linear-gradient(var(--copper),#8a5428);border-radius:0 0 10px 10px;color:#fff;font-family:"Merriweather",serif;font-weight:700;font-size:14px;text-align:center;line-height:30px}
.phone{left:854px;top:44px;display:flex;align-items:center;gap:8px;color:#fff;font-style:italic;font-size:22px;font-family:"Arimo",sans-serif}
.nav{left:334px;top:95px;width:695px;height:36px;display:flex;background:var(--navy-deep);border-radius:10px 10px 0 0;overflow:hidden}
.nav a{flex:auto;color:#fff;text-decoration:none;font-family:"Merriweather",serif;font-size:15px;line-height:36px;text-align:center;border-left:1px solid #2a6a3a}
.nav a.active{background:var(--maroon);border:0;clip-path:polygon(10px 0,100% 0,100% 100%,0 100%)}
.frame{left:138px;top:131px;width:905px;height:831px;background:rgba(225,238,250,.55)}
.banner{left:149px;top:141px;width:884px;height:323px;background:linear-gradient(180deg,#cfe3c4 0%,#6e8f3c 30%,#8aa7a2 55%,#3f5a2a 100%)}
.banner-caption{left:149px;top:429px;width:884px;height:35px;background:rgba(120,30,45,.8);color:#fff;font-family:"Merriweather",serif;font-size:15.5px;line-height:35px;text-align:center;white-space:nowrap}
.arrow{top:294px}
.panel{left:148px;top:499px;width:885px;height:463px;background:var(--panel)}
h2{font-weight:400;font-size:21px;color:var(--brown-head);border-bottom:1px dashed var(--rule);padding-bottom:4px}
h2 b{font-weight:700}
h2 em{font-style:normal;color:var(--navy-deep)}
.welcome{left:159px;top:522px;width:633px}
.welcome p{font-size:12.6px;line-height:16.6px;text-align:justify;margin-top:7px}
.more{left:710px;top:678px;width:87px;font-size:12.5px;font-weight:700;font-style:italic;text-align:right}
.events-head{left:159px;top:725px;width:633px}
.events-nav{left:766px;top:731px;color:#555;font-size:14px}
.events{left:159px;top:766px;width:635px;height:109px;background:linear-gradient(#fafafa,#e4e4e2);border:1px solid #d0d0d0;border-radius:7px;box-shadow:0 10px 10px -6px rgba(0,0,0,.35)}
.event{position:absolute;top:16px;display:flex;gap:11px}
.event-thumb{width:75px;height:58px;background:linear-gradient(135deg,#b9b94a,#7c6a3a 60%,#c9c462)}
.event time{display:block;font-size:13.5px;color:var(--navy-deep);font-weight:700;letter-spacing:.5px}
.event p{font-size:12.4px;line-height:17px;width:220px;margin-top:3px}
.ad-head{left:836px;top:522px;width:177px}
.ad{left:836px;top:565px;width:177px;height:226px;background:linear-gradient(180deg,#3e7fb3 0%,#1a2a4a 55%,#e4e6ea 78%,#f2f2f2 100%);border:4px solid #c6c6c6}
.advertise{left:836px;top:806px;width:177px;height:67px;background:var(--rose);border:1px solid #e0b9c4;color:#fff;font-weight:700;font-size:18px;text-align:center;padding-top:11px;line-height:22px;box-shadow:0 8px 8px -5px rgba(0,0,0,.4)}
.news-label{left:159px;top:920px;font-family:"Open Sans",sans-serif;font-weight:600;font-size:12.5px;color:var(--navy-deep);letter-spacing:.3px}
.news-copy{left:385px;top:911px;font-size:12.6px;line-height:16.5px}
.news-input{left:607px;top:911px;width:333px;height:34px;background:#fff;font-family:"Open Sans",sans-serif;font-style:italic;font-size:11.5px;color:#888;padding:10px 16px}
.news-btn{left:940px;top:911px;width:71px;height:34px;background:var(--navy-deep);color:#fff;font-family:"Open Sans",sans-serif;font-weight:600;font-size:14px;text-align:center;line-height:34px}
.foot-nav{left:0;width:1182px;top:977px;text-align:center;color:#fff;font-size:13px;text-shadow:0 0 2px rgba(0,0,0,.35)}
.foot-nav span{margin:0 6px}
.copy{left:0;width:1182px;top:1006px;text-align:center;color:#fff;font-size:11.5px;text-shadow:0 0 2px rgba(0,0,0,.35)}
.social-foot{left:518px;top:1037px}
</style>
</head>
<body>
<div class="scenery" role="img" aria-label="Sky over a pond, green meadow and wildflowers"></div>

<div class="abs logo"><span class="logo-dot"></span>TMRCL</div>
<div class="abs site-title">TEXAS MARSH REED CONSERVATION LEAGUE</div>

<div class="abs social social-top" aria-label="Social links"><span></span><span></span><span></span><span></span><span></span></div>
<div class="abs join">Become A Member</div>
<div class="abs phone">
  <svg width="30" height="30" viewBox="0 0 30 30"><circle cx="15" cy="15" r="13.5" fill="none" stroke="#0c1f4f" stroke-width="2"/><path d="M11 8c-2 1-2 4 0 8s5 6 7 6l2-2-3-3-2 1c-1-1-2-3-3-5l1-2-2-3z" fill="#0c1f4f"/></svg>
  123-456-7890
</div>

<nav class="abs nav">
  <a class="active" href="#">Home</a><a href="#">About Us</a><a href="#">Members</a><a href="#">Resources</a><a href="#">Events</a><a href="#">Membership</a><a href="#">Contact Us</a>
</nav>

<div class="abs frame"></div>
<div class="abs banner" role="img" aria-label="Tall reeds beside a calm marsh pond"></div>
<div class="abs banner-caption">PROMOTING ENVIRONMENTAL STEWARDSHIP THROUGH OPERATIONS, RESEARCH, EDUCATION &amp; OUTREACH</div>
<svg class="abs arrow" style="left:94px" width="26" height="42" viewBox="0 0 26 42"><path d="M22 3 5 21l17 18" fill="none" stroke="#fff" stroke-width="5"/></svg>
<svg class="abs arrow" style="left:1061px" width="26" height="42" viewBox="0 0 26 42"><path d="M4 3l17 18L4 39" fill="none" stroke="#fff" stroke-width="5"/></svg>

<div class="abs panel"></div>

<section class="abs welcome">
  <h2>Welcome to <em>TEXAS MARSH REED CONSERVATION LEAGUE</em></h2>
  <p>Lorem ipsum dolor sit amet, consectetuer adipiscing elit, sed diam nonummy nibh euismod tincidunt ut laoreet dolore magna aliquam erat volutpat. Ut wisi enim ad minim veniam, quis nostrud exerci tation ullamcorper suscipit lobortis nisl ut aliquip ex ea commodo consequat. Duis autem vel eum iriure dolor in laoreet dolore erat volutpat. Ut wisi enim ad minim veniam, quis nostrud exerci tation laoreet dolore magna aliquam erat volutpat. Ut wisi enim ad minim veniam, quis nostrud exerci tation hendrerit in vulputate velit esse molestie consequat, vel illum dolore eu feugiat nulla facilisis at vero eros et accumsan et iusto odio dignissim qui blandit praesent luptatum zzril delenit augue duis dolore te feugait nulla facilisi.</p>
</section>
<div class="abs more">Read More [+]</div>

<section class="abs events-head"><h2>Upcoming Events</h2></section>
<div class="abs events-nav">‹ ›</div>
<div class="abs events">
  <div class="event" style="left:18px">
    <div class="event-thumb" role="img" aria-label="Water lilies on a pond"></div>
    <div><time>15 Aug, 2014</time><p>Lorem ipsum&nbsp; sed lore, fadrdolors sit amet, consectetuer adipiloresc rererg elit, sed diam nonummy ref nibh Lorema.</p></div>
  </div>
  <div class="event" style="left:353px">
    <div class="event-thumb" role="img" aria-label="Water lilies on a pond"></div>
    <div><time>20 Aug, 2014</time><p>Lorem ipsum&nbsp; sed lore, fadrdolors sit amet, consectetuer adipiloresc rererg elit, sed diam nonummy ref nibh Lorema.</p></div>
  </div>
</div>

<section class="abs ad-head"><h2><b>Advertisement</b></h2></section>
<div class="abs ad" role="img" aria-label="Member advertisement: PondBright Max water treatment by Clearwell Labs"></div>
<div class="abs advertise">ADVERTISE<br>WITH US</div>

<div class="abs news-label">SIGN UP FOR OUR NEWSLETTER</div>
<div class="abs news-copy">Lorem ipsum&nbsp; sed lore, fadrdolors<br>sit amet, consectetuer</div>
<div class="abs news-input">Enter your Email Address</div>
<div class="abs news-btn">SIGNUP</div>

<div class="abs foot-nav">Home <span>|</span> About Us <span>|</span> Members <span>|</span> Resources <span>|</span> Events <span>|</span> Membership <span>|</span> Contact Us</div>
<div class="abs copy">Copyright © 2014,&nbsp; TMRCL | All rights reserved.</div>
<div class="abs social social-foot" aria-label="Social links"><span></span><span></span><span></span><span></span><span></span></div>
</body>
</html>
```